Brochure Design Project for Building Designer

I need a modern and edgy brochure to introduce my new business TORV Design, Commercial and Residential Building Designers.

We specialise in Building Design, Project Management and Design Consultation.

I would like the brochure to be anywhere between 2-4 pages, depending of amount of suitable content available.
Colours to be black and white with splashes of
bright colours (mostly incorporated in photos).

Main Content of brochure to be broken up into 3 (maybe 4) sections to include:

About Us
Services
Projects

Logo Text (DESIGN etc) can be changed to white if suits better with black background.

Would be nice to include sketches to give it that architectural feel.

Samples and wording will be uploaded shortly
Updates

I HAVE PROVIDED A COMPLETE UPDATE OF PROJECT REQUIREMENTS INCLUDING ALL NEW UPLOADED FILES.

PLEASE REFER TO THE BROCHURE LAYOUT PDF UPLOADEDĀ FOR FULL INFORMATION ON PROJECT INCLUDING BROCHURE LAYOUT.

IF YOU HAVE ANY QUESTIONS OR REQUIRE ANY FURTHER INFORMATION, PLEASE LET ME KNOW

I HAVE ADDED FURTHER DEVELOPED PDF DOCUMENTS OF BROCHURE.

IF YOU HAVE TROUBLE OPENING THESE DOCS IN ADOBE ILLUSTRATOR THRU ADOBE BRIDGE PLEASE LET ME KNOW & I WILL UPLOAD AI FILES.

CAN YOU PLEASE FINE TUNE GRAPHICS AND WORK ON BACKGROUND

Target Market(s)

Builders, Property Developers, Architects, Consultants, Professionals

Industry/Entity Type

Business

Requirements
Must have
• Very Professional Look
Black and White
Simple and easy to read layout
Either A4 (if only 2 pages) or
A3 double sided with centre fold (if 4 pages)
Touch up of photos (if possible) to make them stand out of the page.
Samples of recent projects with photos
Should not have
• Any comics or similar

```html
<!DOCTYPE html>
<html lang="en">
<head>
<meta charset="utf-8">
<title>TORV Design – Services</title>
<link href="https://fonts.googleapis.com/css2?family=Arimo:wght@400;700&family=Tinos:wght@700&display=swap" rel="stylesheet">
<style>
  :root {
    --ink: #1b1b1b;
    --paper: #ffffff;
    --brand-pink: #e8559a;
    --panel-dark: #2a2a2a;
    --panel-mid: #4a4a4a;
    --band-light: rgba(255,255,255,0.22);
    --list-text: #ffffff;
    --heading-fill: #3a3a3a;
    --heading-edge: #f2f2f2;
  }
  * { box-sizing: border-box; margin: 0; padding: 0; }
  html, body { width: 850px; height: 1200px; overflow: hidden; background: var(--paper); }
  .brochure {
    position: relative; width: 850px; height: 1200px; overflow: hidden;
    background: var(--paper); font-family: "Arimo", Arial, sans-serif; color: var(--ink);
  }
  .edge-bar { position: absolute; left: 0; width: 850px; background: var(--ink); }
  .edge-bar.top { top: 0; height: 9px; }
  .edge-bar.bottom { bottom: 0; height: 13px; }

  .brand { position: absolute; left: 34px; top: 28px; display: flex; align-items: center; gap: 12px; }
  .brand-mark { width: 26px; height: 26px; background: var(--brand-pink); }
  .brand-name {
    font-family: "Arimo", Arial, sans-serif; font-weight: 700; font-size: 62px;
    letter-spacing: 3px; color: var(--brand-pink); line-height: 1;
  }
  .tagline {
    position: absolute; left: 36px; top: 121px; font-size: 9.5px; font-weight: 400;
    letter-spacing: 0.2px; color: var(--ink);
  }

  .photo-strip { position: absolute; left: 0; display: flex; width: 850px; }
  .photo-strip.upper { top: 137px; height: 144px; }
  .photo-strip.lower { top: 782px; height: 188px; }
  .photo { height: 100%; }

  .services-heading {
    position: absolute; left: 18px; top: 238px; font-family: "Tinos", "Times New Roman", serif;
    font-weight: 700; font-size: 78px; line-height: 1; letter-spacing: 1px;
    color: var(--heading-fill);
    text-shadow: 2px 2px 0 var(--heading-edge), 5px 5px 6px rgba(0,0,0,0.6);
  }

  .services-panel {
    position: absolute; left: 0; top: 317px; width: 850px; height: 465px;
    background: linear-gradient(180deg, #5a5a5a 0%, var(--panel-mid) 35%, var(--panel-dark) 100%);
  }
  .services-panel .highlight-band {
    position: absolute; left: 0; top: 0; width: 850px; height: 270px;
    background: linear-gradient(180deg, var(--band-light), rgba(255,255,255,0.05));
    border-radius: 0 0 28px 0;
  }
  .service-list {
    position: absolute; left: 32px; top: 14px; list-style: none;
  }
  .service-list li {
    font-weight: 700; font-size: 21px; line-height: 45px; color: var(--list-text);
    letter-spacing: 0.3px; text-shadow: 1px 1px 2px rgba(0,0,0,0.5);
  }
  .service-list li::before { content: "-"; display: inline-block; width: 20px; }

  .contact {
    position: absolute; left: 34px; top: 1008px; font-size: 23.5px; line-height: 27px;
    color: var(--ink); font-style: normal;
  }
  .floor-plan {
    position: absolute; left: 459px; top: 970px; width: 383px; height: 215px;
    background: linear-gradient(135deg, #f4f4f4, #d9d9d9); border: 1px solid #777;
  }
</style>
</head>
<body>
<main class="brochure">
  <div class="edge-bar top"></div>

  <header>
    <div class="brand">
      <span class="brand-name">TORV DESIGN</span>
      <span class="brand-mark"></span>
    </div>
    <p class="tagline">COMMERCIAL &amp; RESIDENTIAL BUILDING DESIGNERS</p>
  </header>

  <div class="photo-strip upper">
    <div class="photo" style="width:298px;background:linear-gradient(180deg,#6f8a5a,#8c4a3c 60%,#5a3a30);" role="img" aria-label="Street view of a commercial shopfront with trees"></div>
    <div class="photo" style="width:221px;background:linear-gradient(180deg,#e8ecee,#bfc6c8);" role="img" aria-label="Bright modern dining room interior"></div>
    <div class="photo" style="width:192px;background:linear-gradient(180deg,#0f1a2a,#8a6a55 55%,#3e7f86);" role="img" aria-label="Apartment building at dusk with a pool"></div>
    <div class="photo" style="width:139px;background:linear-gradient(180deg,#5b86b8,#f0f0f0 70%,#8aa27a);" role="img" aria-label="White multi-level beach house"></div>
  </div>

  <h1 class="services-heading">SERVICES</h1>

  <section class="services-panel" role="img" aria-label="Dimmed bedroom interior photograph behind the service list">
    <div class="highlight-band"></div>
    <ul class="service-list">
      <li>PROJECT PLANNING</li>
      <li>DESIGN CONCEPTS</li>
      <li>DESIGN DEVELOPMENT/DEVELOPMENT APPROVAL</li>
      <li>CONSULTANT LIAISON &amp; MANAGEMENT</li>
      <li>BUILDING CERTIFICATION</li>
      <li>TENDER/CONSTRUCTION DOCUMENTATION</li>
      <li>PROJECT MANAGEMENT</li>
      <li>3D MODELLING &amp; RENDERS</li>
      <li>RE-DOCUMENTATION &amp; DESIGN CONSULTATION</li>
      <li>DRAFTING SERVICES</li>
    </ul>
  </section>

  <div class="photo-strip lower">
    <div class="photo" style="width:263px;background:linear-gradient(180deg,#f0f0ee,#c9cbc8 60%,#6d8a88);" role="img" aria-label="Open-plan living and dining interior"></div>
    <div class="photo" style="width:223px;background:linear-gradient(180deg,#2f5fa8,#e6e6e6 55%,#1e1e1e);" role="img" aria-label="Modern commercial building facade"></div>
    <div class="photo" style="width:246px;background:linear-gradient(180deg,#2a2118,#a8783f 50%,#103a2a);" role="img" aria-label="Lit courtyard with swimming pool at night"></div>
    <div class="photo" style="width:118px;background:linear-gradient(180deg,#f2ede4,#c7b9a2 60%,#3a2c22);" role="img" aria-label="Double-height dining room interior"></div>
  </div>

  <address class="contact">
    TORV Design<br>
    PO Box 482, Kelmscott WA 6991<br>
    0400 153 927<br>
    hello@torvdesign.example<br>
    www.torvdesign.example
  </address>

  <div class="floor-plan" role="img" aria-label="Architectural floor plan drawing of a residence"></div>

  <div class="edge-bar bottom"></div>
</main>
</body>
</html>
```